4th Generation Family Business Needs a New Card Design!

We are a family owned 4th Generation company. We are based in the Sydney, Australia area and we are desperately in need of a more modern and classy card. We are monumental masons who design, supply & erect lasting memorials throughout cemeteries in Sydney. Our customers are normally in a period of grieving. I have attached logo files that will need to be implemented on the card. Company was established 1935. Australian Owned and Operated. Card needs to be designed to PRINTLY.com specification.

Target Market(s)

Our target market is based upon people that a grieving for family members that have passed away. We also deal with alot of companies that own and operate cemeteries.

Industry/Entity Type

Business

Contact Information for Business Card

Gavin Pelham, Operations Manager, 0491726053, gavin@pelhamstoneworks.com.au
Brian Pelham, Director, 0417639285, brian@pelhamstoneworks.com.au
Phone # 02 9563 4820
Website: www.pelhamstoneworks.com.au
Address: Suite 17, 9 Lambert Lane, Kellyville, Sydney NSW 2155

Font styles to use
Serif
Decorative
Script

Requirements
Must have
• Would like to see the logo nicely implemented with a modern design. Embossed lettering would be a nice additive.

```html
<!DOCTYPE html>
<html lang="en">
<head>
<meta charset="UTF-8">
<title>Pelham Stoneworks – Business Card</title>
<link rel="stylesheet" href="https://fonts.googleapis.com/css2?family=Roboto+Slab:wght@300;400;700&display=swap">
<style>
  :root {
    --backdrop: #eef0ee;
    --card: #fbfbfa;
    --gold: #e3b95a;
    --gold-deep: #d9a93f;
    --gold-text: #e6b027;
    --ink: #1f1f1f;
    --rule: #555;
  }
  * { margin: 0; padding: 0; box-sizing: border-box; }
  html, body { width: 1200px; height: 1000px; overflow: hidden; }
  body {
    background: var(--backdrop);
    font-family: "Roboto Slab", Georgia, serif;
    color: var(--ink);
    position: relative;
  }
  .card {
    position: absolute;
    top: 352px;
    width: 520px;
    height: 297px;
    background: var(--card);
    box-shadow: 0 10px 28px rgba(0,0,0,0.12), 0 2px 4px rgba(0,0,0,0.08);
    overflow: hidden;
  }
  .card--front { left: 50px; }
  .card--back { left: 630px; }

  /* Front */
  .brand-mark {
    position: absolute;
    top: 26px;
    right: 30px;
    display: flex;
    align-items: center;
    gap: 10px;
  }
  .brand-mark__square {
    width: 30px; height: 30px;
    background: var(--gold);
  }
  .brand-mark__name {
    font-weight: 400;
    font-size: 13px;
    line-height: 1.15;
    letter-spacing: 2px;
    color: var(--ink);
    text-transform: uppercase;
  }
  .person {
    position: absolute;
    left: 32px;
    top: 104px;
  }
  .person__name {
    font-weight: 700;
    font-size: 21px;
    letter-spacing: 0.5px;
    color: var(--gold-text);
    text-transform: uppercase;
  }
  .person__role {
    font-weight: 700;
    font-size: 13px;
    margin-top: 2px;
  }
  .contact {
    position: absolute;
    left: 32px;
    top: 162px;
    width: 420px;
    list-style: none;
  }
  .contact__item {
    font-weight: 700;
    font-size: 10.5px;
    line-height: 1;
    padding: 7px 0 5px;
    border-bottom: 1.5px dotted var(--rule);
    white-space: nowrap;
  }
  .contact__item:first-child { border-top: 1.5px dotted var(--rule); }

  /* Back */
  .band {
    position: absolute;
    left: 0; right: 0;
    top: 70px;
    height: 130px;
    background: linear-gradient(90deg, var(--gold-deep) 0, var(--gold) 12px, var(--gold) 100%);
    display: flex;
    flex-direction: column;
    align-items: center;
    justify-content: center;
  }
  .band__name {
    font-weight: 300;
    color: #fff;
    text-transform: uppercase;
    text-align: center;
    line-height: 1.05;
  }
  .band__name-main { display: block; font-size: 46px; letter-spacing: 4px; }
  .band__name-sub { display: block; font-size: 19px; letter-spacing: 6px; margin-top: 4px; }
  .website {
    position: absolute;
    top: 212px;
    left: 0; right: 0;
    text-align: center;
    font-weight: 700;
    font-size: 12px;
  }
</style>
</head>
<body>
  <section class="card card--front" aria-label="Business card front">
    <div class="brand-mark">
      <span class="brand-mark__square"></span>
      <span class="brand-mark__name">Pelham<br>Stoneworks</span>
    </div>
    <div class="person">
      <h1 class="person__name">Gavin Pelham</h1>
      <p class="person__role">Operation Manager</p>
    </div>
    <ul class="contact">
      <li class="contact__item">P: 02 9563 4820</li>
      <li class="contact__item">E: gavin@pelhamstoneworks.com.au</li>
      <li class="contact__item">L: Suite 17, 9 Lambert Lane, Kellyville, Sydney NSW 2155</li>
      <li class="contact__item">www.pelhamstoneworks.com.au</li>
    </ul>
  </section>

  <section class="card card--back" aria-label="Business card back">
    <div class="band">
      <p class="band__name">
        <span class="band__name-main">Pelham</span>
        <span class="band__name-sub">Stoneworks</span>
      </p>
    </div>
    <p class="website">www.pelhamstoneworks.com.au</p>
  </section>
</body>
</html>
```